High End Clothing Line Needs Stationary Design

We need a stationery design including letterhead and envelopes for a new Christian clothing company called Covenant 9 based out of New York. Our company colors are charcoal gray and silver. The final design needs to be modern, simple, and have a high end look to it.

Industry/Entity Type

Clothing

Font styles to use
Sans Serif

Colors
474747
cfcfcf

Requirements
Must have
• On the top of page in center we would like a dark gray solid box with logo inside in light gray. Name, email, title, phone # must be on bottom of the page.
• Light gray cross will be on black flap of envelope. Entire back flap in dark gray. Eventually logo and cross will be done in silver stamping when project complete.
Nice to have
• Would like to see how just the logo without Covenant 9 looks in middle of letterhead faded in background.

```html
<!DOCTYPE html>
<html lang="en">
<head>
<meta charset="utf-8">
<title>Covenant 9 Stationery</title>
<link rel="stylesheet" href="https://fonts.googleapis.com/css2?family=Carlito:wght@400;700&family=Montserrat:wght@400;600&display=swap">
<style>
  :root {
    --charcoal: #474747;
    --silver: #cfcfcf;
    --backdrop: #c0c0c0;
    --paper: #ffffff;
    --ink: #1e1e1e;
    --faint: #efefef;
  }
  * { box-sizing: border-box; margin: 0; padding: 0; }
  html, body { width: 1200px; height: 640px; overflow: hidden; }
  body {
    background: var(--backdrop);
    position: relative;
    font-family: "Carlito", "Calibri", sans-serif;
    color: var(--ink);
  }

  /* Brand block */
  .brand-box {
    position: absolute;
    background: var(--charcoal);
    border-radius: 3px;
    display: flex;
    align-items: center;
    justify-content: center;
  }
  .brand-name {
    font-family: "Carlito", sans-serif;
    font-weight: 400;
    color: var(--silver);
    text-align: center;
    line-height: 1;
  }
  .brand-watermark {
    position: absolute;
    font-family: "Carlito", sans-serif;
    font-weight: 400;
    color: var(--faint);
    white-space: nowrap;
    line-height: 1;
    pointer-events: none;
  }

  /* Letterhead */
  .letterhead {
    position: absolute;
    left: 73px; top: 38px;
    width: 417px; height: 540px;
    background: var(--paper);
    overflow: hidden;
  }
  .letterhead .brand-box { left: 176px; top: 13px; width: 66px; height: 66px; }
  .letterhead .brand-name { font-size: 13px; }
  .letterhead .brand-watermark {
    left: 50%; top: 250px;
    transform: translateX(-50%);
    font-size: 62px;
  }
  .letter-body {
    position: absolute;
    left: 38px; top: 107px;
    width: 342px;
    font-size: 7.6px;
    line-height: 14px;
  }
  .letter-body p { margin-bottom: 14px; }
  .letter-body .closing { margin-bottom: 0; }
  .signature {
    width: 100px; height: 30px;
    background: linear-gradient(90deg, #eef2f8, #dfe6f1);
    border-radius: 2px;
    margin: 0 0 6px;
  }
  .letter-footer {
    position: absolute;
    left: 0; bottom: 0;
    width: 100%; height: 34px;
    background: var(--charcoal);
    color: var(--paper);
    font-family: "Montserrat", sans-serif;
    text-align: center;
    padding-top: 7px;
  }
  .letter-footer .contact-row {
    display: flex; justify-content: center; gap: 8px;
    font-size: 5.2px;
  }
  .letter-footer .address {
    font-size: 5.6px; font-weight: 600; margin-top: 5px;
  }
  .contact-item { display: inline-flex; align-items: center; gap: 3px; }
  .icon { width: 6px; height: 6px; fill: currentColor; }

  /* Envelope front */
  .envelope-front {
    position: absolute;
    left: 560px; top: 73px;
    width: 557px; height: 236px;
    background: var(--paper);
    overflow: hidden;
  }
  .envelope-front .brand-box { left: 14px; top: 13px; width: 56px; height: 56px; }
  .envelope-front .brand-name { font-size: 11px; }
  .envelope-front .brand-watermark {
    right: 12px; bottom: 12px;
    font-size: 60px;
  }
  .return-address {
    position: absolute;
    left: 15px; top: 77px;
    font-family: "Montserrat", sans-serif;
    color: #444;
    font-size: 5.4px;
    line-height: 9.4px;
  }
  .return-address .contact-item { display: flex; }
  .return-address .address {
    color: var(--ink); font-weight: 600; line-height: 8px; margin-top: 2px;
  }

  /* Envelope back */
  .envelope-back {
    position: absolute;
    left: 560px; top: 342px;
    width: 557px; height: 236px;
    background: var(--paper);
    overflow: hidden;
  }
  .envelope-flap { position: absolute; left: 0; top: 0; width: 557px; height: 69px; }
  .flap-stamp {
    position: absolute;
    left: 272px; top: 27px;
    width: 13px; height: 13px;
    background: var(--silver);
  }
</style>
</head>
<body>

  <section class="letterhead">
    <div class="brand-box"><span class="brand-name">Covenant 9</span></div>
    <div class="brand-watermark" aria-hidden="true">Covenant 9</div>

    <div class="letter-body">
      <p>Lorem Ipsum is simply</p>
      <p>&nbsp;dummy text of the printing and typesetting industry. Lorem Ipsum has been the industry's standard dummy text ever since the 1500s, when an unknown printer took a galley of type and scrambled it to make a type specimen book. It has survived not only five centuries, but also the leap into electronic typesetting, remaining essentially unchanged.</p>
      <p>It is a long established fact that a reader will be distracted by the readable content of a page when looking at its layout. The point of using Lorem Ipsum is that it has a more-or-less normal distribution of letters, as opposed to using 'Content here, content here', making it look like readable English.</p>
      <p>&nbsp;Contrary to popular belief, Lorem Ipsum is not simply random text. It has roots in a piece of classical Latin literature from 45 BC, making it over 2000 years old. Daniel Ashford, a Latin professor at Westbrook College in Virginia, looked up one of the more obscure Latin words, consectetur, from a Lorem Ipsum passage, and going through the cites of the word in classical literature, discovered the undoubtable source. Lorem Ipsum comes from sections 1.10.32 and 1.10.33 of "de Finibus Bonorum et Malorum" (The Extremes of Good and Evil) by Tavian Morel, written in 45 BC. This book</p>
      <p class="closing">Lorem Ipsum</p>
      <div class="signature" role="img" aria-label="Handwritten signature"></div>
      <p>Lorem Ipsum is a dummy</p>
    </div>

    <footer class="letter-footer">
      <div class="contact-row">
        <span class="contact-item">
          <svg class="icon" viewBox="0 0 10 10"><path d="M2 1h2l1 2-1.2 1a6 6 0 0 0 2.2 2.2L7 5l2 1v2a1 1 0 0 1-1 1A8 8 0 0 1 1 2a1 1 0 0 1 1-1z"/></svg>(000) 555-0148
        </span>
        <span class="contact-item">
          <svg class="icon" viewBox="0 0 10 10"><path d="M1 2h8v6H1z M1.5 2.5 5 5.5l3.5-3" fill="none" stroke="currentColor" stroke-width="1"/></svg>hello@covenant9.example
        </span>
        <span class="contact-item">
          <svg class="icon" viewBox="0 0 10 10"><g fill="none" stroke="currentColor" stroke-width="0.9"><circle cx="5" cy="5" r="4"/><ellipse cx="5" cy="5" rx="1.8" ry="4"/><path d="M1 5h8"/></g></svg>www.covenant9.example
        </span>
      </div>
      <div class="address">210 Harbor Lane, Albany, New York 12207</div>
    </footer>
  </section>

  <section class="envelope-front">
    <div class="brand-box"><span class="brand-name">Covenant 9</span></div>
    <div class="brand-watermark" aria-hidden="true">Covenant 9</div>
    <div class="return-address">
      <span class="contact-item">
        <svg class="icon" viewBox="0 0 10 10"><path d="M2 1h2l1 2-1.2 1a6 6 0 0 0 2.2 2.2L7 5l2 1v2a1 1 0 0 1-1 1A8 8 0 0 1 1 2a1 1 0 0 1 1-1z"/></svg>(000) 555-0148
      </span>
      <span class="contact-item">
        <svg class="icon" viewBox="0 0 10 10"><path d="M1 2h8v6H1z M1.5 2.5 5 5.5l3.5-3" fill="none" stroke="currentColor" stroke-width="1"/></svg>hello@covenant9.example
      </span>
      <span class="contact-item">
        <svg class="icon" viewBox="0 0 10 10"><g fill="none" stroke="currentColor" stroke-width="0.9"><circle cx="5" cy="5" r="4"/><ellipse cx="5" cy="5" rx="1.8" ry="4"/><path d="M1 5h8"/></g></svg>www.covenant9.example
      </span>
      <div class="address">210 Harbor Lane<br>Albany, New York 12207</div>
    </div>
  </section>

  <section class="envelope-back">
    <svg class="envelope-flap" viewBox="0 0 557 69" aria-hidden="true">
      <path d="M0 0H557L525 8C518 30 515 69 500 69H58C42 69 40 30 33 8Z" fill="var(--charcoal)"/>
    </svg>
    <div class="flap-stamp" role="img" aria-label="Silver stamped cross mark"></div>
  </section>

</body>
</html>
```